Our product is called "BrisaVeil Antimicrobial Photosensitizer Mask." It is worn over the face by individuals who have respiratory infections. It releases singlet oxygen upon contact with visible light. So, this product will be sold to the healthcare industry and in retail establishments to individuals with respiratory infections.
This website must have the look and feel of being professional and clean. So, a white background is where I think I want this website to end up. Though, I am open to designs that have different color backgrounds like a light to medium gray or black.. In other words I prefer a white background, but I do not want to constrain the artists who might have other unique ideas about how the website should appear.
The logo files are attached to this brief. #ff3e81 is the hex color code that is used in the mask. The green shade in the cloud and light rays surrounding the mask should be used as well.
Target Market(s)
Health and wellness
Industry/Entity Type
Healthcare
Coding
Number of Pages Required
5+ page
Requirements
Must have
- Pages: Home, Our Company, Contact, FAQ page, Order, Terms and Conditions, Legal

```html
<!DOCTYPE html>
<html lang="en">
<head>
<meta charset="utf-8">
<title>BrisaVeil – Legal</title>
<link href="https://fonts.googleapis.com/css2?family=Poppins:wght@300;400;500;600;700&display=swap" rel="stylesheet">
<style>
:root{
  --yellow:#f9fc3f;
  --green:#13804c;
  --pink:#ff6b9d;
  --pink-deep:#ff3e81;
  --pink-light:#f9b0cb;
  --pink-band:#f4afc6;
  --ink:#111111;
  --body:#444444;
  --footer:#161616;
  --footer-base:#262626;
  --muted:#9a9a9a;
  --white:#ffffff;
}
*{margin:0;padding:0;box-sizing:border-box}
html,body{width:854px;height:1200px;overflow:hidden;background:var(--white)}
body{position:relative;font-family:'Poppins',sans-serif;color:var(--ink)}
.abs{position:absolute}
.topbar{left:0;top:0;width:854px;height:26px;background:var(--yellow)}
.topbar .contact{left:44px;top:6px;font-size:10px;color:var(--ink);display:flex;gap:12px;align-items:center}
.contact span{display:flex;align-items:center;gap:5px}
.social{display:flex;gap:11px}
.social i{display:block;width:15px;height:15px;border-radius:50%;background:var(--ink)}
.topbar .social{right:50px;top:5px}
.nav{left:0;top:26px;width:854px;height:107px;background:var(--green)}
.brand{left:50px;top:26px;width:110px;height:54px;display:flex;align-items:center;gap:6px}
.brand b{display:block;width:16px;height:16px;border-radius:50%;background:var(--pink-deep)}
.brand span{font-weight:600;font-size:16px;color:var(--white)}
.menu{right:44px;top:44px;display:flex;gap:31px;font-size:13px;font-weight:500;color:var(--white)}
.hero{left:0;top:133px;width:854px;height:294px}
.hero-title{left:44px;top:224px;font-size:42px;font-weight:700;color:var(--white);letter-spacing:.5px}
.hero-sub{left:44px;top:287px;font-size:14.5px;color:var(--white)}
.hero-photo{left:470px;top:190px;width:310px;height:237px;background:linear-gradient(160deg,#e9c9a0 0%,#3c4456 45%,#c4ccc8 75%,#f4afc6 100%);border-radius:40px 40px 0 0;opacity:.85}
.terms-title{left:0;top:482px;width:854px;text-align:center;font-size:28px;font-weight:600;line-height:39px;color:var(--ink)}
.intro{left:0;top:589px;width:854px;text-align:center;font-size:11.5px;color:#555}
.clause{left:44px;width:760px}
.clause h3{font-size:11.5px;font-weight:600;color:var(--ink);margin-bottom:4px}
.clause p{font-size:9px;color:var(--body)}
.footer{left:0;top:887px;width:854px;height:279px;background:var(--footer)}
.footer-base{left:0;top:1166px;width:854px;height:34px;background:var(--footer-base);color:#ccc;font-size:7.5px;text-align:center;line-height:34px}
.footer-brand{left:60px;top:935px;width:170px;height:170px;border-radius:50%;background:radial-gradient(circle,#2d3a1e 0%,#1c2414 55%,var(--footer) 72%);display:flex;align-items:center;justify-content:center;gap:7px}
.footer-brand b{display:block;width:18px;height:18px;border-radius:50%;background:var(--pink-deep)}
.footer-brand span{font-weight:600;font-size:18px;color:var(--pink-deep)}
.fh{font-size:16px;font-weight:400;color:var(--white)}
.small{font-size:8.5px;color:var(--muted);line-height:15.5px}
.footer .social i{background:#bdbdbd;width:16px;height:16px}
.quick{display:flex;flex-direction:column;gap:11px;font-size:11px;color:var(--white)}
.legal-links{left:0;top:1145px;width:854px;display:flex;justify-content:center;gap:9px;font-size:9px;color:#ccc}
</style>
</head>
<body>
<div class="abs topbar">
  <div class="abs contact">
    <span><svg width="10" height="10" viewBox="0 0 24 24"><path fill="#111" d="M6.6 10.8a15 15 0 0 0 6.6 6.6l2.2-2.2a1 1 0 0 1 1-.25 11.4 11.4 0 0 0 3.6.57 1 1 0 0 1 1 1V20a1 1 0 0 1-1 1A17 17 0 0 1 3 4a1 1 0 0 1 1-1h3.5a1 1 0 0 1 1 1c0 1.25.2 2.45.57 3.57a1 1 0 0 1-.25 1z"/></svg>014 220 7315</span>
    <span><svg width="12" height="9" viewBox="0 0 24 18"><rect x="1" y="1" width="22" height="16" fill="none" stroke="#111" stroke-width="2"/><path d="M1 1l11 9 11-9" fill="none" stroke="#111" stroke-width="2"/></svg>hello@brisaveil-mail.com</span>
  </div>
  <div class="abs social"><i></i><i></i><i></i><i></i><i></i><i></i></div>
</div>

<header class="abs nav">
  <div class="abs brand"><b></b><span>BrisaVeil</span></div>
  <nav class="abs menu"><span>Home</span><span>About Us</span><span>Testimonials</span><span>FAQ</span><span>Contact Us</span><span>Order</span></nav>
</header>

<section class="abs hero">
  <svg width="854" height="294" class="abs" style="left:0;top:0">
    <rect width="854" height="267" fill="var(--pink-light)"/>
    <polygon points="0,0 558,0 394,267 0,267" fill="var(--pink)"/>
    <rect x="117" y="267" width="737" height="27" fill="var(--pink-band)"/>
  </svg>
</section>
<div class="abs hero-photo" role="img" aria-label="Photo of two women in pink masks reading a map together"></div>
<h1 class="abs hero-title">LEGAL</h1>
<p class="abs hero-sub">Legal Notice</p>

<h2 class="abs terms-title">Terms of Use for BrisaVeil<br>Website and Products</h2>
<p class="abs intro">By using the BrisaVeil website and purchasing our products, you agree to adhere to the following legal terms:</p>

<div class="abs clause" style="top:663px"><h3>1. Intellectual Property</h3><p>All content on this website, including logos, trademarks, text, and images, are the intellectual property of BrisaVeil. Unauthorized use of this content is prohibited.</p></div>
<div class="abs clause" style="top:719px"><h3>2. Limitation of Liability</h3><p>BrisaVeil’s liability is limited to the purchase price of the product. We are not liable for any indirect or consequential damages.</p></div>
<div class="abs clause" style="top:775px"><h3>3. Indemnification</h3><p>You agree to indemnify and hold harmless BrisaVeil from any claims, damages, or expenses arising from your use of our products or website.</p></div>
<p class="abs clause" style="top:820px;font-size:9px;color:var(--body)">For full details on our legal policies, please refer to the full Terms and Conditions and Privacy Policy sections.</p>

<footer class="abs footer"></footer>
<div class="abs footer-brand"><b></b><span>BrisaVeil</span></div>
<h4 class="abs fh" style="left:339px;top:928px">Get in touch</h4>
<p class="abs" style="left:339px;top:974px;font-size:13px;color:var(--muted)">(555) 210-8834</p>
<div class="abs social" style="left:339px;top:1014px"><i></i><i></i><i></i><i></i><i></i><i></i></div>
<h4 class="abs fh" style="left:547px;top:928px">Location</h4>
<p class="abs small" style="left:547px;top:973px">48 Harbor Lane, Suite 2C,<br>Portland, OR 9720</p>
<h4 class="abs fh" style="left:547px;top:1025px">Hours</h4>
<p class="abs small" style="left:547px;top:1068px">Mon - Sat : 9 AM – 5 PM<br>Sunday: Closed</p>
<h4 class="abs fh" style="left:716px;top:928px">Quick Links</h4>
<div class="abs quick" style="left:716px;top:977px"><span>Home</span><span>About</span><span>Testimonials</span><span>FAQ</span><span>Contact Us</span><span>Order</span></div>
<div class="abs legal-links"><span>Site Owner</span><span>Cookies Notice</span><span>Privacy Notice</span><span>Legal</span></div>
<div class="abs footer-base">2025 © BrisaVeil.&nbsp; All rights reserved.</div>
</body>
</html>
```